Website Revamp: Favorzo.com

Just got a new logo looking for a web design to go with the business. I need the photoshop files and stock photos. No Word Press Please.

```html
<!DOCTYPE html>
<html lang="en">
<head>
<meta charset="utf-8">
<title>Favorzo Auto Recycling</title>
<link href="https://fonts.googleapis.com/css2?family=Raleway:wght@400;500;600;700&display=swap" rel="stylesheet">
<style>
:root{
  --green:#8cc63f;
  --green-dark:#79b12f;
  --ink:#222222;
  --text:#555555;
  --muted:#888888;
  --light:#f3f3f3;
  --footer:#232323;
  --white:#ffffff;
  --slate:#6f7b7c;
}
*{box-sizing:border-box;margin:0;padding:0}
html,body{width:1200px;height:4178px;overflow:hidden}
body{position:relative;background:var(--white);font-family:'Raleway',sans-serif;color:var(--text)}
.btn{position:absolute;display:flex;align-items:center;justify-content:center;gap:10px;background:var(--green);color:var(--white);border-radius:30px;font-size:13px;font-weight:500}
.section-title{position:absolute;left:0;width:1200px;text-align:center;font-weight:500;letter-spacing:.5px;color:var(--ink)}
.divider{position:absolute;left:520px;width:160px;height:24px;display:flex;align-items:center;justify-content:space-between}
.divider span{width:58px;height:2px;background:currentColor}

/* header */
.site-header{position:absolute;top:0;left:0;width:1200px;height:110px;background:var(--white);z-index:3}
.brand-badge{position:absolute;left:82px;top:-20px;width:130px;height:168px;border-radius:0 0 65px 65px;background:var(--white);z-index:4;display:flex;flex-direction:column;align-items:center;justify-content:flex-end;padding-bottom:34px;gap:6px}
.brand-dot{width:56px;height:56px;border-radius:50%;background:var(--green)}
.brand-name{font-size:24px;font-weight:700;color:var(--green)}
.main-nav{position:absolute;top:47px;left:489px;font-size:12px;color:var(--ink)}
.main-nav a{position:absolute;white-space:nowrap;text-decoration:none;color:var(--ink)}
.main-nav a.active{color:var(--green)}
.main-nav a.active::after{content:"";position:absolute;left:0;right:0;bottom:-7px;height:1px;background:var(--green)}

/* hero */
.hero{position:absolute;top:110px;left:0;width:1200px;height:620px;background:linear-gradient(180deg,#4a4c4f 0%,#6a6b6d 40%,#515254 75%,#3b3c3e 100%)}
.hero h1{position:absolute;top:253px;width:1200px;text-align:center;font-size:33px;font-weight:700;color:var(--white);letter-spacing:-.5px}
.hero h1 em{font-style:normal;color:var(--green)}
.hero p{position:absolute;top:300px;width:1200px;text-align:center;font-size:13px;line-height:17px;color:var(--white)}
.hero-dots{position:absolute;top:510px;left:574px;display:flex;gap:10px}
.hero-dots i{width:6px;height:6px;border-radius:50%;background:rgba(255,255,255,.5)}
.hero-dots i.on{background:var(--green)}
.hero-wave{position:absolute;top:640px;left:0}

/* about */
.about-photo{position:absolute;left:152px;top:755px;width:420px;height:420px;border-radius:50%;background:radial-gradient(circle at 50% 45%,#b4bcc2 0%,#9aa6a8 55%,#8cc63f 56%,#7fb536 100%)}
.about-heading{position:absolute;left:657px;top:810px;font-size:31px;font-weight:500;color:var(--ink)}
.about-rule{position:absolute;left:581px;top:829px;width:60px;height:3px;background:var(--green)}
.about-copy{position:absolute;left:644px;top:861px;width:442px;font-size:12px;line-height:15px;color:#444}
.about-copy p{margin-bottom:14px}

/* services */
.services{position:absolute;top:1249px;left:0;width:1200px;height:824px;background:linear-gradient(135deg,#8e9898 0%,#a5adac 45%,#8a9494 100%)}
.services .section-title{top:50px;color:var(--white);font-size:32px}
.services .divider{top:101px;color:var(--white)}
.service-card{position:absolute;width:309px;height:256px;background:var(--white);border-radius:5px;text-align:center}
.service-icon{position:absolute;left:114px;top:38px;width:80px;height:50px;background:var(--green);border-radius:6px;opacity:.85}
.service-card h3{position:absolute;top:104px;width:100%;font-size:17px;font-weight:500;color:var(--ink)}
.service-card .bar{position:absolute;top:134px;left:139px;width:32px;height:2px;background:var(--green)}
.service-card p{position:absolute;top:146px;left:40px;width:229px;font-size:12px;line-height:16px;color:#555}
.service-card .go{position:absolute;top:213px;left:145px;width:18px;height:18px;border:1.5px solid #333;border-radius:50%}

/* news */
.news .section-title{top:2140px;font-size:34px}
.news-card{position:absolute;top:2204px;width:333px;height:370px;background:var(--light)}
.news-photo{position:absolute;left:13px;top:13px;width:307px;height:185px}
.news-date{position:absolute;left:8px;top:8px;width:48px;height:48px;background:var(--green);color:var(--white);font-size:13px;font-weight:600;line-height:15px;text-align:center;padding-top:9px}
.news-card h4{position:absolute;left:13px;top:223px;font-size:13px;font-weight:600;color:var(--ink)}
.news-card p{position:absolute;left:13px;top:260px;width:310px;font-size:11.5px;line-height:17px;color:#555}
.news-card a{position:absolute;left:13px;top:343px;font-size:12px;color:#777;text-decoration:underline}

/* contact */
.contact{position:absolute;top:2697px;left:0;width:1200px;height:480px;background:linear-gradient(135deg,#3f4a2c 0%,#55603d 45%,#2f3824 100%)}
.contact .section-title{top:75px;color:var(--white);font-size:32px}
.contact .divider{top:114px;color:var(--white)}
.field{position:absolute;left:295px;width:300px;height:36px;background:var(--white);border:1px solid #ccc;display:flex;align-items:center;gap:9px;padding-left:12px;font-size:12px;color:#555}
.field svg{flex:none}
.field.message{left:608px;width:302px;height:190px;align-items:flex-start;padding-top:10px}

/* testimonials */
.testimonials .section-title{top:3243px;font-size:35px}
.testimonials .sub{position:absolute;top:3291px;width:1200px;text-align:center;font-size:13px;color:var(--ink)}
.avatar{position:absolute;left:538px;top:3335px;width:120px;height:120px;border-radius:50%;background:radial-gradient(circle at 50% 45%,#9aa0a4,#5e6469)}
.quote-badge{position:absolute;left:535px;top:3418px;width:36px;height:36px;border-radius:50%;background:var(--green);color:var(--white);font-size:26px;font-weight:700;text-align:center;line-height:44px}
.testimonial-text{position:absolute;top:3482px;left:270px;width:660px;text-align:center;font-size:12px;line-height:18px;color:#555}
.stars{position:absolute;top:3553px;width:1200px;text-align:center;color:#f3a41b;font-size:15px;letter-spacing:4px}
.person{position:absolute;top:3579px;width:1200px;text-align:center;font-size:22px;color:var(--ink)}
.role{position:absolute;top:3617px;width:1200px;text-align:center;font-size:15px;color:var(--muted)}
.t-dots{position:absolute;top:3663px;left:577px;display:flex;gap:12px}
.t-dots i{width:8px;height:8px;border-radius:50%;background:#aaa}
.t-dots i.on{background:var(--green)}

/* footer */
.footer-wave{position:absolute;top:3680px;left:0}
.site-footer{position:absolute;top:3770px;left:0;width:1200px;height:340px;background:var(--footer);color:var(--white)}
.footer-brand{position:absolute;left:84px;top:140px;display:flex;flex-direction:column;align-items:center;gap:10px}
.footer-col h5{position:absolute;top:84px;font-size:18px;font-weight:400}
.footer-col h5::after{content:"";position:absolute;left:0;top:34px;width:40px;height:2px;background:var(--green)}
.footer-links{position:absolute;left:338px;top:140px;list-style:none;font-size:12px;line-height:22.5px}
.footer-links li::before{content:"•";margin-right:8px}
.footer-links li:first-child{font-weight:700}
.footer-contact{position:absolute;left:592px;top:140px;font-size:12px;line-height:24.5px;list-style:none}
.footer-contact li{display:flex;gap:12px;align-items:flex-start}
.footer-contact li svg{margin-top:6px;flex:none}
.footer-contact li.cont{padding-left:24px}
.newsletter p{position:absolute;left:858px;top:137px;width:270px;font-size:12px;line-height:14px}
.newsletter .email{position:absolute;left:858px;top:178px;width:266px;height:34px;border-radius:20px;background:var(--white);color:#999;font-size:12px;padding:10px 17px}
.newsletter .subscribe{position:absolute;left:858px;top:223px;width:266px;height:34px;border-radius:20px;background:var(--green);color:var(--white);font-size:12px;text-align:center;line-height:34px}
.copyright{position:absolute;top:4138px;left:74px;font-size:11.5px;color:#333}
.copyright b{color:var(--green);font-weight:600}
.socials{position:absolute;top:4126px;left:956px;display:flex;gap:11px}
.socials i{width:34px;height:34px;border-radius:50%;background:#222}
.socials i:first-child{background:var(--green)}
</style>
</head>
<body>

<header class="site-header">
  <div class="brand-badge"><span class="brand-dot"></span><span class="brand-name">Favorzo</span></div>
  <nav class="main-nav">
    <a class="active" style="left:0">Home</a>
    <a style="left:73px">About us</a>
    <a style="left:164px">Services &#8964;</a>
    <a style="left:258px">Latest News</a>
    <a style="left:367px">Contact us</a>
  </nav>
  <div class="btn" style="left:970px;top:36px;width:155px;height:40px;font-weight:600">Schedule Pickup</div>
</header>

<section class="hero" role="img" aria-label="Photo of stacked scrapped cars in a salvage yard">
  <h1>WELCOME TO <em>FAVORZO</em></h1>
  <p>Lorem Ipsum simply dummy text of the printing set industry<br>recycling auto in the&nbsp; standard dummy text 1500s,</p>
  <div class="btn" style="left:495px;top:357px;width:186px;height:41px">
    <svg width="18" height="18" viewBox="0 0 18 18" fill="none" stroke="#fff" stroke-width="1.5"><rect x="2" y="3" width="14" height="13" rx="1"/><path d="M2 7h14M6 1v4M12 1v4"/></svg>
    Schedule Pickup
  </div>
  <div class="hero-dots"><i></i><i class="on"></i><i></i><i></i></div>
</section>
<svg class="hero-wave" width="1200" height="92" viewBox="0 0 1200 92">
  <path d="M0 40 C250 -5 520 10 760 40 C950 64 1080 54 1200 20 V92 H0Z" fill="#6f7b7c"/>
  <path d="M0 55 C260 15 520 25 760 52 C960 74 1090 58 1200 30 V92 H0Z" fill="#ffffff"/>
  <path d="M700 78 C900 80 1080 60 1200 15 V40 C1080 80 900 92 700 78Z" fill="#8cc63f"/>
</svg>

<section class="about">
  <div class="about-photo" role="img" aria-label="Round photo of scrapped cars stacked in a recycling yard, framed by a green leaf illustration"></div>
  <span class="about-rule"></span>
  <h2 class="about-heading">ABOUT US</h2>
  <div class="about-copy">
    <p>Lorem Ipsum is simply dummy text of the printing and typesetting an has been the industry's standard dummy text ever since the 1500s,</p>
    <p>when an unknown printer took a galley of type and scrambled it to make a type specimen book. It has survived not only five centuries but also the leap into electronic typesetting, remaining essentially a unchanged. It was popularised in the 1960s</p>
    <p>with the release of Setline sheets containing Lorem Ipsum passages and more recently with desktop publishing software like Pagecraft including versions of Lorem Ipsum.</p>
  </div>
  <div class="btn" style="left:642px;top:1061px;width:175px;height:42px">Read More</div>
</section>

<section class="services" aria-label="Our services">
  <h2 class="section-title">OUR SERVICES</h2>
  <div class="divider"><span></span><svg width="28" height="24" viewBox="0 0 28 24" fill="none" stroke="#fff" stroke-width="2"><path d="M14 2 L26 22 H2 Z"/></svg><span></span></div>
  <div class="service-card" style="left:114px;top:154px"><div class="service-icon" role="img" aria-label="Car with money icon"></div><h3>WE BUY JUNK CARS</h3><span class="bar"></span><p>Lorem Ipsum is simply dummy text of the printing and typesetting industry. standard dummy text 1500s,</p><span class="go"></span></div>
  <div class="service-card" style="left:444px;top:154px"><div class="service-icon" role="img" aria-label="Tow truck lifting car icon"></div><h3>AUTO SALVAGE</h3><span class="bar"></span><p>Lorem Ipsum is simply dummy text of the printing and typesetting industry. standard dummy text 1500s,</p><span class="go"></span></div>
  <div class="service-card" style="left:777px;top:154px"><div class="service-icon" role="img" aria-label="Car with gears icon"></div><h3>JUNK CAR NO TITLE</h3><span class="bar"></span><p>Lorem Ipsum is simply dummy text of the printing and typesetting industry. standard dummy text 1500s,</p><span class="go"></span></div>
  <div class="service-card" style="left:114px;top:435px"><div class="service-icon" role="img" aria-label="Damaged car icon"></div><h3>JUNK NO TITLE</h3><span class="bar"></span><p>Lorem Ipsum is simply dummy text of the printing and typesetting industry. standard dummy text 1500s,</p><span class="go"></span></div>
  <div class="service-card" style="left:444px;top:435px"><div class="service-icon" role="img" aria-label="Cash and car icon"></div><h3>SCRAP IT FOR CASH</h3><span class="bar"></span><p>Lorem Ipsum is simply dummy text of the printing and typesetting industry. standard dummy text 1500s,</p><span class="go"></span></div>
  <div class="service-card" style="left:777px;top:435px"><div class="service-icon" role="img" aria-label="Truck towing car icon"></div><h3>TOW JUNK CARS</h3><span class="bar"></span><p>Lorem Ipsum is simply dummy text of the printing and typesetting industry. standard dummy text 1500s,</p><span class="go"></span></div>
  <div class="btn" style="left:511px;top:733px;width:174px;height:41px">View More</div>
</section>

<section class="news">
  <h2 class="section-title">LATEST NEWS</h2>
  <article class="news-card" style="left:73px"><div class="news-photo" role="img" aria-label="Photo of a car loaded on a tow truck" style="background:linear-gradient(160deg,#8d97a0,#4f6b57)"><div class="news-date">02<br>Mar</div></div><h4>News 01</h4><p>Lorem Ipsum is simply dummy text of the printing and typesetting industry Lorem Ipsum been the industry's dummy text ever since the 1500s,</p><a>Read More</a></article>
  <article class="news-card" style="left:433px"><div class="news-photo" role="img" aria-label="Photo of a rusty vintage car" style="background:linear-gradient(160deg,#a09a8c,#6a5c48)"><div class="news-date">02<br>Mar</div></div><h4>News 01</h4><p>Lorem Ipsum is simply dummy text of the printing and typesetting industry Lorem Ipsum been the industry's dummy text ever since the 1500s,</p><a>Read More</a></article>
  <article class="news-card" style="left:790px"><div class="news-photo" role="img" aria-label="Photo of cars stacked on racks in a scrapyard" style="background:linear-gradient(160deg,#5a5f68,#3b3f58)"><div class="news-date">02<br>Mar</div></div><h4>News 01</h4><p>Lorem Ipsum is simply dummy text of the printing and typesetting industry Lorem Ipsum been the industry's dummy text ever since the 1500s,</p><a>Read More</a></article>
  <div class="btn" style="left:522px;top:2595px;width:143px;height:34px">View More</div>
</section>

<section class="contact" role="img" aria-label="Photo of an abandoned old car overgrown with moss">
  <h2 class="section-title">QUICK CONTACT</h2>
  <div class="divider"><span></span><svg width="28" height="24" viewBox="0 0 28 24" fill="none" stroke="#8cc63f" stroke-width="2"><path d="M14 2 L26 22 H2 Z"/></svg><span></span></div>
  <div class="field" style="top:164px"><svg width="12" height="12" viewBox="0 0 12 12" fill="none" stroke="#8cc63f"><circle cx="6" cy="4" r="2.5"/><path d="M1 11c1-3 9-3 10 0"/></svg>Name</div>
  <div class="field" style="top:216px"><svg width="12" height="12" viewBox="0 0 12 12" fill="none" stroke="#8cc63f"><path d="M2 1h3l1 3-2 1c1 2 2 3 3 3l1-2 3 1v3C5 11 1 7 2 1z"/></svg>Phone</div>
  <div class="field" style="top:268px"><svg width="12" height="12" viewBox="0 0 12 12" fill="none" stroke="#8cc63f"><rect x="1" y="2" width="10" height="9"/><path d="M1 5h10"/></svg>Date</div>
  <div class="field" style="top:318px"><svg width="12" height="12" viewBox="0 0 12 12" fill="none" stroke="#8cc63f"><circle cx="6" cy="6" r="5"/><path d="M6 3v3l2 1"/></svg>Time</div>
  <div class="field message" style="top:164px"><svg width="12" height="12" viewBox="0 0 12 12" fill="none" stroke="#8cc63f"><rect x="1" y="2" width="10" height="7"/><path d="M3 5h6"/></svg>Message</div>
  <div class="btn" style="left:525px;top:380px;width:145px;height:32px">Send Now</div>
</section>

<section class="testimonials">
  <h2 class="section-title">TESTIMONIALS</h2>
  <div class="sub">what clients say</div>
  <div class="avatar" role="img" aria-label="Client portrait photo"></div>
  <div class="quote-badge">&ldquo;</div>
  <p class="testimonial-text">Lorem Ipsum is simply dummy text of the printing and typesetting industry. Lorem Ipsum has been the industry's standard dummy text ever since the 1500s, when an unknown printer took a galley of type and scrambled it to make a type specimen book. It has survived not only five centuries,</p>
  <div class="stars">★★★★★</div>
  <div class="person">Daniel Marsh</div>
  <div class="role">Creative Director</div>
  <div class="t-dots"><i class="on"></i><i></i><i></i></div>
</section>

<svg class="footer-wave" width="1200" height="92" viewBox="0 0 1200 92">
  <path d="M0 30 C200 -5 420 15 700 50 C900 72 1080 55 1200 20 V92 H0Z" fill="#6f7b7c"/>
  <path d="M0 62 C250 28 480 40 720 62 C940 80 1090 68 1200 40 V92 H0Z" fill="#232323"/>
  <path d="M700 66 C900 70 1080 50 1200 5 V30 C1080 70 900 82 700 66Z" fill="#8cc63f"/>
</svg>
<footer class="site-footer">
  <div class="footer-brand"><span class="brand-dot" style="width:64px;height:64px"></span><span class="brand-name" style="font-size:26px">Favorzo</span></div>
  <div class="footer-col"><h5 style="left:336px">Quick Link</h5></div>
  <ul class="footer-links"><li>Home</li><li>About us</li><li>Services</li><li>Latest News</li><li>Contact us</li></ul>
  <div class="footer-col"><h5 style="left:592px">Quick Contact</h5></div>
  <ul class="footer-contact">
    <li><svg width="12" height="13" viewBox="0 0 12 13" fill="none" stroke="#fff"><path d="M6 12S1.5 7.5 1.5 5a4.5 4.5 0 019 0C10.5 7.5 6 12 6 12z"/><circle cx="6" cy="5" r="1.5"/></svg>48 Alder Lane, Westbrook,</li>
    <li class="cont">New York 10991,</li>
    <li class="cont">USA</li>
    <li><svg width="12" height="12" viewBox="0 0 12 12" fill="none" stroke="#fff"><rect x="1" y="3" width="10" height="8" rx="1"/><path d="M3 3V1h6v2"/></svg>800-555-0148</li>
    <li><svg width="12" height="10" viewBox="0 0 12 10" fill="none" stroke="#fff"><rect x="0.5" y="0.5" width="11" height="9"/><path d="M0.5 0.5l5.5 5 5.5-5"/></svg>sales@Favorzo.com</li>
  </ul>
  <div class="footer-col"><h5 style="left:860px">Join Our Newletter</h5></div>
  <div class="newsletter">
    <p>Lorem Ipsum is simply dummy&nbsp; the printing and typesetting industry.</p>
    <div class="email">Email Here</div>
    <div class="subscribe">Subscribe</div>
  </div>
</footer>

<div class="copyright">Copyright © 2020 <b>Favorzo</b> <strong>Auto Recycling</strong>. All Right Reserved</div>
<div class="socials" aria-label="Social links"><i></i><i></i><i></i><i></i></div>

</body>
</html>
```